Website banner

Here is the link where the current banner is featured https://www.brimlark.com.au/collections/gel-blasters

I need the banner recreated into desktop and mobile format size.
Update the key points to:
- FREE SHIPPING AUSTRALIA WIDE
- SAME DAY DISPATCH
- BEST PRICE GUARANTEE
- 3000+ 5 STAR REVIEWS
- BEST SERVICE & WARRANTY
- 100% SECURE CHECKOUT

I want the banner to suit the style of the website and make it look better than the last graphic.

I also need the "save even more" picture to be recreated as it looks very plain at the moment,

```html
<!DOCTYPE html>
<html lang="en">
<head>
<meta charset="UTF-8">
<title>Gel Blasters Banner</title>
<link href="https://fonts.googleapis.com/css2?family=Bebas+Neue&family=Poppins:wght@600;700&display=swap" rel="stylesheet">
<style>
  :root {
    --page-bg: #e6e7e8;
    --photo-dark: #1e1a16;
    --photo-mid: #3d3428;
    --photo-light: #5a4c3a;
    --brand-red: #d40d0d;
    --deep-red: #5c0606;
    --text-white: #ffffff;
    --star-gold: #f5c518;
    --map-blue: #1c2f8a;
    --map-blue-light: #3a52b4;
  }
  html, body {
    margin: 0;
    padding: 0;
    width: 1200px;
    height: 900px;
    overflow: hidden;
    background: var(--page-bg);
  }
  .banner {
    position: absolute;
    left: 0;
    top: 267px;
    width: 1200px;
    height: 366px;
    overflow: hidden;
  }
  .banner__photo {
    position: absolute;
    inset: 0;
    background:
      radial-gradient(ellipse 45% 70% at 48% 45%, var(--photo-light) 0%, rgba(90,76,58,0) 70%),
      radial-gradient(ellipse 30% 60% at 20% 70%, rgba(80,68,52,0.8) 0%, rgba(80,68,52,0) 70%),
      linear-gradient(90deg, var(--photo-dark) 0%, var(--photo-mid) 45%, var(--photo-dark) 100%);
  }
  .reviews {
    position: absolute;
    left: 109px;
    top: 112px;
    width: 220px;
    text-align: center;
    color: var(--text-white);
    font-family: "Poppins", sans-serif;
  }
  .reviews__title {
    margin: 0;
    font-weight: 700;
    font-size: 25px;
    line-height: 31px;
  }
  .reviews__stars {
    display: flex;
    justify-content: center;
    gap: 3px;
    margin-top: 10px;
  }
  .reviews__label {
    margin: 8px 0 0;
    font-weight: 600;
    font-size: 17px;
    letter-spacing: 0.3px;
  }
  .perks {
    position: absolute;
    left: 396px;
    top: 72px;
    margin: 0;
    padding: 0;
    list-style: none;
  }
  .perk {
    display: flex;
    align-items: center;
    height: 52px;
    margin-bottom: 7.5px;
  }
  .perk__icon {
    width: 54px;
    height: 50px;
    flex: none;
  }
  .perk__text {
    margin-left: 20px;
    font-family: "Bebas Neue", sans-serif;
    font-size: 37px;
    letter-spacing: 1px;
    color: var(--text-white);
    text-shadow: 0 2px 4px rgba(0,0,0,0.6);
    padding-top: 4px;
  }
  .shipping {
    position: absolute;
    left: 882px;
    top: 80px;
    width: 318px;
    height: 45px;
    background: var(--brand-red);
    border-radius: 22px 0 0 22px;
    font-family: "Poppins", sans-serif;
  }
  .shipping__title {
    position: absolute;
    left: 27px;
    top: 1px;
    margin: 0;
    font-weight: 700;
    font-size: 22px;
    letter-spacing: 0.6px;
    color: var(--text-white);
  }
  .shipping__sub {
    position: absolute;
    left: 27px;
    top: 28px;
    margin: 0;
    font-weight: 600;
    font-size: 10px;
    letter-spacing: 1.5px;
    color: var(--deep-red);
  }
  .country-map {
    position: absolute;
    left: 874px;
    top: 148px;
    width: 160px;
    height: 145px;
    border-radius: 30px 40px 45px 35px;
    background: radial-gradient(ellipse at 40% 35%, var(--map-blue-light) 0%, var(--map-blue) 75%);
    box-shadow: 0 6px 12px rgba(0,0,0,0.5);
  }
</style>
</head>
<body>
  <section class="banner">
    <div class="banner__photo" role="img" aria-label="Dark, hazy photo of soldiers in camouflage aiming rifles"></div>

    <div class="reviews">
      <h2 class="reviews__title">3000+ 5 STARS<br>REVIEWS</h2>
      <div class="reviews__stars" aria-label="5 out of 5 stars">
        <svg width="31" height="30" viewBox="0 0 24 23"><polygon fill="var(--star-gold)" points="12,0 15,8 24,8.5 17,14 19.5,23 12,18 4.5,23 7,14 0,8.5 9,8"/></svg>
        <svg width="31" height="30" viewBox="0 0 24 23"><polygon fill="var(--star-gold)" points="12,0 15,8 24,8.5 17,14 19.5,23 12,18 4.5,23 7,14 0,8.5 9,8"/></svg>
        <svg width="31" height="30" viewBox="0 0 24 23"><polygon fill="var(--star-gold)" points="12,0 15,8 24,8.5 17,14 19.5,23 12,18 4.5,23 7,14 0,8.5 9,8"/></svg>
        <svg width="31" height="30" viewBox="0 0 24 23"><polygon fill="var(--star-gold)" points="12,0 15,8 24,8.5 17,14 19.5,23 12,18 4.5,23 7,14 0,8.5 9,8"/></svg>
        <svg width="31" height="30" viewBox="0 0 24 23"><polygon fill="var(--star-gold)" points="12,0 15,8 24,8.5 17,14 19.5,23 12,18 4.5,23 7,14 0,8.5 9,8"/></svg>
      </div>
      <p class="reviews__label">HIGHEST&nbsp; RATED</p>
    </div>

    <ul class="perks">
      <li class="perk">
        <svg class="perk__icon" viewBox="0 0 54 50">
          <polygon fill="var(--brand-red)" points="13,0 41,0 54,25 41,50 13,50 0,25"/>
          <path fill="var(--text-white)" d="M15 25 L19 22 L25 23 L21 14 L24 14 L31 23 L37 23 Q40 25 37 27 L31 27 L24 36 L21 36 L25 27 L19 28 Z"/>
        </svg>
        <span class="perk__text">SAME DAY DISPATCH</span>
      </li>
      <li class="perk">
        <svg class="perk__icon" viewBox="0 0 54 50">
          <polygon fill="var(--brand-red)" points="13,0 41,0 54,25 41,50 13,50 0,25"/>
          <text x="27" y="35" text-anchor="middle" fill="var(--text-white)" font-family="Poppins, sans-serif" font-weight="700" font-size="28">$</text>
        </svg>
        <span class="perk__text">BEST PRICE + GUARANTEE</span>
      </li>
      <li class="perk">
        <svg class="perk__icon" viewBox="0 0 54 50">
          <polygon fill="var(--brand-red)" points="13,0 41,0 54,25 41,50 13,50 0,25"/>
          <rect x="17" y="23" width="5" height="12" fill="var(--text-white)"/>
          <path fill="var(--text-white)" d="M23 23 L27 17 Q28 13 30 14 Q31 16 30 21 L36 21 Q38 22 37 24 Q38 26 36.5 27 Q37.5 29 35.5 30 Q36 33 33 34 L23 34 Z"/>
        </svg>
        <span class="perk__text">BEST SERVICE &amp; WARRANTY</span>
      </li>
      <li class="perk">
        <svg class="perk__icon" viewBox="0 0 54 50">
          <polygon fill="var(--brand-red)" points="13,0 41,0 54,25 41,50 13,50 0,25"/>
          <path fill="none" stroke="var(--text-white)" stroke-width="2.2" d="M27 13 L37 17 L37 25 Q37 33 27 38 Q17 33 17 25 L17 17 Z"/>
          <rect x="23" y="24" width="8" height="7" rx="1" fill="var(--text-white)"/>
          <path fill="none" stroke="var(--text-white)" stroke-width="1.8" d="M24.5 24 L24.5 22 Q27 18.5 29.5 22 L29.5 24"/>
        </svg>
        <span class="perk__text">100% SECURE CHECKOUT</span>
      </li>
    </ul>

    <div class="shipping">
      <p class="shipping__title">FREE SHIPPING</p>
      <p class="shipping__sub">AUSTRALIA WIDE</p>
    </div>

    <div class="country-map" role="img" aria-label="Map of Australia filled with the Australian flag"></div>
  </section>
</body>
</html>
```